Startup Technology Consulting Firm in NYC Needs A Website

I need a website built for my startup technology consulting company Larkspur Systems Group. We offer a unique white glove service that provides end to end technology support. I want to stand out above the rest. We are small firm but are very dedicated which where we derive our name from LSG primarily offers
end to end technology advisory services to small businesses lacking their own IT staff. We offer top notch white glove and our customer service and satisfaction is exceed by no one.

Below are some of what we provide our clients

Strategic IT Planning
Business Continuity Planning/Disaster Recovery
Cloud Computing\DataCenter Solutions
Server Infrastructure/Networking
Virtualization Technologies
Project Management

Our Technology Advisors hold many certifications from Quorvane & Zelpix. We are also Quorvane Partners

I have attached my logo (preview design) As soon as I ge the final images I will upload.

Industry/Entity Type

Information Technology

Coding

Coded - Design and coding required

Number of Pages Required

1 page

Font styles to use
Sans Serif

Requirements
Must have
• Attract Target Market. The site should bleed the company vision
• DEDICATION everything about the site should show this
• Layout the Benefits of our offerings
• Links to my social media
• Links to dircct my client's for remote support

```html
<!DOCTYPE html>
<html lang="en">
<head>
<meta charset="utf-8">
<title>Larkspur Systems Group</title>
<link href="https://fonts.googleapis.com/css2?family=Roboto:wght@400;500;700&display=swap" rel="stylesheet">
<style>
:root{
  --navy:#0d2a6b;
  --blue:#1a8fd6;
  --ink:#333;
  --muted:#7a7a7a;
  --line:#e3e3e3;
  --footer:#2b2b2b;
  --footer-text:#cfcfcf;
  --white:#fff;
}
*{box-sizing:border-box;margin:0;padding:0}
html,body{width:923px;height:1200px;overflow:hidden;background:var(--white)}
body{position:relative;font-family:"Roboto",Arial,sans-serif;color:var(--ink)}
a{color:inherit;text-decoration:none}
.abs{position:absolute}

/* header */
.brand{left:76px;top:58px;color:var(--navy);font-weight:500;line-height:1}
.brand-name{font-size:19px;letter-spacing:.5px;display:flex;align-items:center;gap:7px}
.brand-dot{width:12px;height:12px;border-radius:50%;background:var(--blue)}
.brand-sub{font-size:8.5px;letter-spacing:1.6px;margin:4px 0 0 19px}
.phone{right:77px;top:27px;font-size:12.5px;color:var(--muted);display:flex;align-items:center;gap:5px}
.phone strong{color:var(--ink);font-weight:400}
.nav{right:77px;top:70px;display:flex;gap:27px;font-size:9.6px;letter-spacing:.4px;color:#555}
.nav .active{color:var(--navy)}

/* hero */
.hero{left:0;top:114px;width:923px;height:329px;background:linear-gradient(100deg,#3a3a3a 0%,#6e6e6e 35%,#8d8d8d 55%,#5a5a5a 100%)}
.hero-title{left:76px;top:72px;font-size:27px;font-weight:700;color:var(--white)}
.hero-arrow{top:152px;width:20px;height:26px;background:rgba(40,40,40,.75);display:flex;align-items:center;justify-content:center}

/* welcome */
.welcome-title{left:0;width:923px;top:488px;text-align:center;font-size:27px;font-weight:700;color:var(--blue);letter-spacing:.5px}
.welcome-title span{color:var(--navy)}
.welcome-text{left:115px;width:693px;top:524px;text-align:center;font-size:9px;line-height:17px;color:var(--muted)}
.certified{left:316px;top:608px;display:flex;align-items:center;font-size:10px;color:var(--ink)}
.partner{display:flex;align-items:center;gap:5px;font-size:17px;color:#666;font-weight:400}
.partner-mark{width:20px;height:20px;background:#9a9a9a}
.divider{left:76px;top:674px;width:770px;height:1px;background:var(--line)}

/* services */
.service{width:236px}
.service-icon{height:32px}
.service-title{font-size:13px;font-weight:500;color:var(--navy);line-height:16px}
.service-text{font-size:8.5px;line-height:14.5px;color:var(--muted)}
.service-bar{width:236px;height:3px;background:var(--blue)}

/* footer */
.footer{left:0;top:1127px;width:923px;height:73px;background:var(--footer)}
.footer-links{left:76px;top:20px;font-size:8.5px;color:var(--footer-text);display:flex;gap:6px}
.footer-copy{left:76px;top:41px;font-size:8.5px;color:var(--footer-text)}
.social{top:26px;width:22px;height:22px;border-radius:50%}
</style>
</head>
<body>

<header>
  <div class="abs brand" aria-label="Larkspur Systems Group">
    <div class="brand-name"><span class="brand-dot"></span>LARKSPUR</div>
    <div class="brand-sub">SYSTEMS GROUP</div>
  </div>
  <div class="abs phone">
    <svg width="10" height="10" viewBox="0 0 24 24"><path fill="#7a7a7a" d="M6.6 10.8a15 15 0 006.6 6.6l2.2-2.2c.3-.3.7-.4 1-.2 1.1.4 2.3.6 3.6.6.6 0 1 .4 1 1V20c0 .6-.4 1-1 1A17 17 0 013 4c0-.6.4-1 1-1h3.5c.6 0 1 .4 1 1 0 1.3.2 2.5.6 3.6.1.3 0 .7-.2 1z"/></svg>
    Call us on - <strong>555 014 2297</strong>
  </div>
  <nav class="abs nav">
    <a class="active" href="#">HOME</a>
    <a href="#">ABOUT US</a>
    <a href="#">SERVICES</a>
    <a href="#">SOLUTIONS</a>
    <a href="#">CONTACT US</a>
  </nav>
</header>

<section class="abs hero" role="img" aria-label="Photo of a businessman pushing a large white chess knight across a chessboard toward black pieces">
  <h1 class="abs hero-title">Strategic IT Planning</h1>
  <div class="abs hero-arrow" style="left:0"><svg width="8" height="14" viewBox="0 0 8 14"><path d="M7 1L1 7l6 6" stroke="#ddd" fill="none"/></svg></div>
  <div class="abs hero-arrow" style="right:0"><svg width="8" height="14" viewBox="0 0 8 14"><path d="M1 1l6 6-6 6" stroke="#ddd" fill="none"/></svg></div>
</section>

<section>
  <h2 class="abs welcome-title">WELCOME TO <span>LSG</span></h2>
  <p class="abs welcome-text">Aenean sed quam non sapien faucibus consequat vitae sit amet orci. Praesent quis risus mi. In mollis nulla in pulvinar dictum. Vivamus interdum sagittis felis, ut dapibus ligula feugiat ac. In dictum sapien eu tellus finibus fermentum. Aenean faucibus lacus ut mollis commodo. Donec vestibulum odio sem, ac laoreet massa ullamcorper id. Donec molestie nisi et tellus hendrerit vehicula. Nunc eu ligula sed quam pulvinar maximus in vitae eros. Proin porta fermentum ipsum, vel porttitor turpis venenatis luctus. Vivamus volutpat eu sapien quis tempus. Aenean feugiat viverra lorem ac sagittis.</p>
  <div class="abs certified">
    <span style="margin-right:20px">Certified By</span>
    <span class="partner" style="margin-right:20px"><span class="partner-mark"></span>Quorvane</span>
    <span class="partner">Zelpix</span>
  </div>
  <div class="abs divider"></div>
</section>

<section>
  <article class="abs service" style="left:77px;top:730px">
    <svg class="service-icon" width="24" height="32" viewBox="0 0 24 32"><circle cx="12" cy="6" r="5" fill="#1a8fd6"/><rect x="10" y="11" width="4" height="10" fill="#1a8fd6"/><path d="M5 24h14l3 5H2z" fill="#1a8fd6"/><rect x="0" y="29" width="24" height="3" fill="#0d2a6b"/></svg>
    <h3 class="abs service-title" style="top:51px">Strategic IT Planning</h3>
    <p class="abs service-text" style="top:89px">Sed augue orci, elementum in magna congue, tincidunt vulputate erat. Aliquam consectetur orci molestie dictum molestie. Proin eget congue nulla, vel tempor diam.</p>
    <div class="abs service-bar" style="top:140px"></div>
  </article>
  <article class="abs service" style="left:344px;top:730px">
    <svg class="service-icon" width="31" height="31" viewBox="0 0 31 31"><rect x="1.5" y="1.5" width="28" height="28" fill="none" stroke="#1a8fd6" stroke-width="3"/><rect x="7" y="15" width="4" height="10" fill="#1a8fd6"/><rect x="13.5" y="9" width="4" height="16" fill="#1a8fd6"/><rect x="20" y="12" width="4" height="13" fill="#1a8fd6"/></svg>
    <h3 class="abs service-title" style="top:51px">Business Continuity Planning/Disaster Recovery</h3>
    <p class="abs service-text" style="top:89px">Sed augue orci, elementum in magna congue, tincidunt vulputate erat. Aliquam consectetur orci molestie dictum molestie. Proin eget congue nulla, vel tempor diam.</p>
    <div class="abs service-bar" style="top:140px"></div>
  </article>
  <article class="abs service" style="left:610px;top:730px">
    <svg class="service-icon" width="47" height="30" viewBox="0 0 47 30"><path d="M10 30a9 9 0 01-1-18 13 13 0 0125-3 10 10 0 013 21z" fill="#1a8fd6"/></svg>
    <h3 class="abs service-title" style="top:51px">Cloud Computing\DataCenter Solutions</h3>
    <p class="abs service-text" style="top:89px">Sed augue orci, elementum in magna congue, tincidunt vulputate erat. Aliquam consectetur orci molestie dictum molestie. Proin eget congue nulla, vel tempor diam.</p>
    <div class="abs service-bar" style="top:140px"></div>
  </article>

  <article class="abs service" style="left:77px;top:948px">
    <svg class="service-icon" width="28" height="28" viewBox="0 0 28 28"><rect x="1.5" y="1.5" width="25" height="25" fill="none" stroke="#1a8fd6" stroke-width="3"/><rect x="6" y="7" width="16" height="5" fill="none" stroke="#1a8fd6" stroke-width="2"/><rect x="6" y="16" width="16" height="5" fill="none" stroke="#1a8fd6" stroke-width="2"/></svg>
    <h3 class="abs service-title" style="top:46px">Server Infrastructure/Networking</h3>
    <p class="abs service-text" style="top:69px">Sed augue orci, elementum in magna congue, tincidunt vulputate erat. Aliquam consectetur orci molestie dictum molestie. Proin eget congue nulla, vel tempor diam.</p>
    <div class="abs service-bar" style="top:119px"></div>
  </article>
  <article class="abs service" style="left:344px;top:948px">
    <svg class="service-icon" width="35" height="30" viewBox="0 0 35 30"><rect x="1.5" y="1.5" width="32" height="21" fill="none" stroke="#1a8fd6" stroke-width="3"/><rect x="15" y="23" width="5" height="4" fill="#0d2a6b"/><rect x="11" y="27" width="13" height="3" fill="#0d2a6b"/></svg>
    <h3 class="abs service-title" style="top:46px">Virtualisation Technologies</h3>
    <p class="abs service-text" style="top:69px">Sed augue orci, elementum in magna congue, tincidunt vulputate erat. Aliquam consectetur orci molestie dictum molestie. Proin eget congue nulla, vel tempor diam.</p>
    <div class="abs service-bar" style="top:119px"></div>
  </article>
  <article class="abs service" style="left:610px;top:948px">
    <svg class="service-icon" width="30" height="30" viewBox="0 0 30 30"><rect x="10" y="0" width="10" height="8" fill="#1a8fd6"/><path d="M15 8v5M5 13h20M5 13v5M15 13v5M25 13v5" stroke="#0d2a6b" stroke-width="2" fill="none"/><rect x="0" y="18" width="9" height="5" fill="#1a8fd6"/><rect x="10.5" y="18" width="9" height="5" fill="#1a8fd6"/><rect x="21" y="18" width="9" height="5" fill="#1a8fd6"/><rect x="0" y="24" width="9" height="5" fill="#1a8fd6"/><rect x="21" y="24" width="9" height="5" fill="#1a8fd6"/></svg>
    <h3 class="abs service-title" style="top:46px">Project Management</h3>
    <p class="abs service-text" style="top:69px">Sed augue orci, elementum in magna congue, tincidunt vulputate erat. Aliquam consectetur orci molestie dictum molestie. Proin eget congue nulla, vel tempor diam.</p>
    <div class="abs service-bar" style="top:119px"></div>
  </article>
</section>

<footer class="abs footer">
  <nav class="abs footer-links">
    <a href="#">Home</a><span>|</span><a href="#">About Us</a><span>|</span><a href="#">Services</a><span>|</span><a href="#">Solutions</a><span>|</span><a href="#">Contact Us</a>
  </nav>
  <p class="abs footer-copy">Copyright &copy; 2015 &nbsp;Larkspur Systems Group. &nbsp;All rights reserved</p>
  <a class="abs social" href="#" aria-label="Social profile one" style="left:771px;background:#3b5998"></a>
  <a class="abs social" href="#" aria-label="Social profile two" style="left:798px;background:#1da1f2"></a>
  <a class="abs social" href="#" aria-label="Social profile three" style="left:825px;background:#0e76a8"></a>
</footer>

</body>
</html>
```